Business Card Design

We are looking for a double sided business card.

On one side would be our logo

On the Other Side

Martin Kolby
Sales and Marketing

Phone/Text Logo and 530-418-2763
Email Logo and info@plumvalepets.com
Website Logo and www.plumvalepets.com
Facebook Logo and plumvale pets
Instagram Logo and plumvale_pets

Target Market(s)

Pet owners

Contact Information for Business Card

In project description

Requirements
Must have
• Logo

```html
<!DOCTYPE html>
<html lang="en">
<head>
<meta charset="utf-8">
<title>Plumvale Pets – Business Card</title>
<link rel="stylesheet" href="https://fonts.googleapis.com/css2?family=Montserrat:wght@400;500;700&display=swap">
<style>
  :root {
    --page: #3a3a3c;
    --paper: #ffffff;
    --ink: #1f1f1f;
    --card-dark: #1c1c1c;
    --orange: #f08a1c;
    --amber: #f5b921;
    --silver: #c9c9c9;
  }
  html, body {
    margin: 0;
    width: 1200px;
    height: 1200px;
    overflow: hidden;
    background: var(--page);
    font-family: "Montserrat", sans-serif;
  }
  .card {
    position: absolute;
    width: 720px;
    height: 410px;
    border-radius: 28px;
    overflow: hidden;
    box-sizing: border-box;
  }
  /* Contact side */
  .card-front {
    left: 80px;
    top: 100px;
    background: var(--paper);
  }
  .front-band {
    position: absolute;
    left: 0; right: 0; bottom: 0;
    height: 44px;
    display: flex;
  }
  .front-band .band-warm {
    flex: 0 0 64%;
    background: linear-gradient(90deg, var(--orange), var(--amber));
  }
  .front-band .band-gap { flex: 0 0 8px; background: var(--paper); }
  .front-band .band-dark { flex: 1; background: var(--ink); }

  .contact-block {
    position: absolute;
    left: 52px;
    top: 62px;
    color: var(--ink);
  }
  .person-name {
    margin: 0;
    font-size: 34px;
    font-weight: 500;
    letter-spacing: 0.5px;
    color: var(--orange);
    text-transform: uppercase;
  }
  .person-role {
    margin: 2px 0 22px;
    font-size: 19px;
    font-weight: 400;
  }
  .contact-list, .social-list {
    list-style: none;
    margin: 0;
    padding: 0;
  }
  .contact-list li, .social-list li {
    display: flex;
    align-items: center;
    gap: 12px;
    font-size: 19px;
    line-height: 32px;
  }
  .social-list { margin-top: 16px; }
  .icon { width: 22px; height: 22px; flex: none; }

  .front-brand {
    position: absolute;
    right: 54px;
    top: 120px;
    text-align: center;
  }
  .brand-name {
    display: flex;
    align-items: center;
    gap: 12px;
    margin: 0;
    font-weight: 700;
    letter-spacing: 1px;
    text-transform: uppercase;
  }
  .brand-dot {
    border-radius: 50%;
    background: var(--orange);
    flex: none;
  }
  .front-brand .brand-name { font-size: 34px; color: var(--orange); }
  .front-brand .brand-dot { width: 26px; height: 26px; }

  /* Logo side */
  .card-back {
    left: 400px;
    top: 660px;
    background: var(--card-dark);
    border-bottom: 4px solid var(--orange);
    display: flex;
    align-items: center;
    justify-content: center;
  }
  .card-back .brand-name { font-size: 46px; color: var(--orange); }
  .card-back .brand-dot { width: 34px; height: 34px; }
</style>
</head>
<body>

<section class="card card-front" aria-label="Business card, contact side">
  <div class="contact-block">
    <h1 class="person-name">Martin Kolby</h1>
    <p class="person-role">Sales and Marketing</p>
    <ul class="contact-list">
      <li>
        <svg class="icon" viewBox="0 0 24 24" aria-hidden="true"><path fill="#f08a1c" d="M6.6 10.8a15.1 15.1 0 0 0 6.6 6.6l2.2-2.2a1 1 0 0 1 1-.25 11.4 11.4 0 0 0 3.6.57 1 1 0 0 1 1 1V20a1 1 0 0 1-1 1A17 17 0 0 1 3 4a1 1 0 0 1 1-1h3.5a1 1 0 0 1 1 1c0 1.25.2 2.45.57 3.57a1 1 0 0 1-.25 1z"/></svg>
        530-418-2763
      </li>
      <li>
        <svg class="icon" viewBox="0 0 24 24" aria-hidden="true"><rect x="2" y="5" width="20" height="14" rx="1.5" fill="#f08a1c"/><path d="M2.5 6 12 13l9.5-7" fill="none" stroke="#fff" stroke-width="1.6"/></svg>
        info@plumvalepets.com
      </li>
      <li>
        <svg class="icon" viewBox="0 0 24 24" aria-hidden="true"><g fill="none" stroke="#f08a1c" stroke-width="1.8"><circle cx="12" cy="12" r="9.5"/><ellipse cx="12" cy="12" rx="4.2" ry="9.5"/><path d="M2.5 12h19M4 7h16M4 17h16"/></g></svg>
        www.plumvalepets.com
      </li>
    </ul>
    <ul class="social-list">
      <li>
        <svg class="icon" viewBox="0 0 24 24" aria-hidden="true"><rect x="2" y="2" width="20" height="20" rx="4" fill="none" stroke="#f08a1c" stroke-width="2"/></svg>
        plumvale pets
      </li>
      <li>
        <svg class="icon" viewBox="0 0 24 24" aria-hidden="true"><rect x="2" y="2" width="20" height="20" rx="4" fill="none" stroke="#f08a1c" stroke-width="2"/></svg>
        @plumvale_pets
      </li>
    </ul>
  </div>

  <div class="front-brand">
    <p class="brand-name"><span class="brand-dot"></span>Plumvale Pets</p>
  </div>

  <div class="front-band">
    <span class="band-warm"></span>
    <span class="band-gap"></span>
    <span class="band-dark"></span>
  </div>
</section>

<section class="card card-back" aria-label="Business card, logo side">
  <p class="brand-name"><span class="brand-dot"></span>Plumvale Pets</p>
</section>

</body>
</html>
```